Brixelo Photography Business Cards

We need a good general business card that we can hand to our clients. We will be doing embossed gloss cards.

Target Market(s)

Real estate / Business to business / professionals

```html
<!DOCTYPE html>
<html lang="en">
<head>
<meta charset="UTF-8">
<title>Brixelo Photography Business Cards</title>
<link href="https://fonts.googleapis.com/css2?family=Arimo:wght@400;700&display=swap" rel="stylesheet">
<style>
  :root {
    --navy: #262466;
    --deep: #23206a;
    --blue: #2f9fdc;
    --sky: #3fa9e0;
    --white: #ffffff;
    --ghost: #ecedf2;
    --ink: #2a2770;
    --stage: #2b2b2e;
  }
  * { margin: 0; padding: 0; box-sizing: border-box; }
  html, body { width: 1200px; height: 900px; overflow: hidden; }
  body {
    background: var(--stage);
    font-family: "Arimo", Arial, sans-serif;
    position: relative;
  }
  .card {
    position: absolute;
    width: 600px;
    height: 340px;
    border-radius: 22px;
    overflow: hidden;
    box-shadow: 0 6px 18px rgba(0,0,0,0.45);
  }
  /* Back side */
  .card-back {
    left: 80px; top: 60px;
    background: linear-gradient(35deg, var(--deep) 0%, #2a4f9f 50%, var(--sky) 100%);
  }
  .card-back .faint-motif {
    position: absolute;
    right: 30px; top: 20px;
    width: 260px; height: 240px;
    border-radius: 30px;
    background: radial-gradient(circle, rgba(255,255,255,0.12), rgba(255,255,255,0) 70%);
  }
  .back-brand {
    position: absolute;
    inset: 0;
    display: flex; align-items: center; justify-content: center; gap: 16px;
  }
  .back-brand .mark {
    width: 44px; height: 44px;
    border: 3px solid var(--white);
    border-radius: 50%;
  }
  .back-brand .name {
    color: var(--white);
    font-weight: 700;
    font-size: 34px;
    letter-spacing: 1px;
  }
  /* Front side */
  .card-front {
    left: 520px; top: 480px;
    background: var(--white);
  }
  .card-front .faint-motif {
    position: absolute;
    left: 250px; top: 10px;
    width: 300px; height: 170px;
    background: linear-gradient(135deg, rgba(236,237,242,0) 0%, var(--ghost) 50%, rgba(236,237,242,0) 100%);
  }
  .front-brand {
    position: absolute;
    left: 30px; top: 36px;
    color: var(--navy);
    font-weight: 700;
    font-size: 30px;
  }
  .holder {
    position: absolute;
    right: 0; top: 120px;
    width: 340px;
  }
  .holder .person {
    font-weight: 700;
    font-size: 27px;
    color: var(--ink);
    padding-left: 24px;
  }
  .holder .role-band {
    margin-top: 6px;
    height: 28px;
    background: linear-gradient(90deg, var(--blue), #48b0e4);
    clip-path: polygon(0 0, 100% 0, 100% 100%, 16% 100%);
    color: var(--white);
    font-size: 17px;
    line-height: 28px;
    text-align: right;
    padding-right: 26px;
  }
  .holder .address {
    margin-top: 12px;
    text-align: right;
    padding-right: 26px;
    font-size: 17px;
    line-height: 21px;
    color: var(--ink);
  }
  .divider {
    position: absolute;
    left: 30px; top: 188px;
    width: 250px; height: 1.5px;
    background: var(--navy);
  }
  .contacts {
    position: absolute;
    left: 30px; top: 200px;
    list-style: none;
  }
  .contacts li {
    display: flex; align-items: center; gap: 10px;
    font-size: 19px;
    color: var(--ink);
    height: 30px;
  }
  .contacts svg { width: 22px; height: 22px; flex: none; }
  .base-stripe {
    position: absolute;
    left: 0; bottom: 0;
    width: 100%; height: 12px;
    background: linear-gradient(90deg, var(--blue), #37a6df);
  }
  .corner-block {
    position: absolute;
    right: 0; bottom: 0;
    width: 190px; height: 26px;
    background: var(--navy);
    clip-path: polygon(6% 0, 100% 0, 100% 100%, 0 100%);
  }
</style>
</head>
<body>
  <section class="card card-back" aria-label="Card back">
    <div class="faint-motif" role="img" aria-label="Faint brand decoration"></div>
    <div class="back-brand">
      <span class="mark"></span>
      <span class="name">Brixelo Photography</span>
    </div>
  </section>

  <section class="card card-front" aria-label="Card front">
    <div class="faint-motif" role="img" aria-label="Faint brand decoration"></div>
    <div class="front-brand">Brixelo Photography</div>

    <div class="holder">
      <div class="person">Marcus Delaney</div>
      <div class="role-band">Manager</div>
      <div class="address">Your address, city<br>state, ZIP 0000</div>
    </div>

    <div class="divider"></div>
    <ul class="contacts">
      <li>
        <svg viewBox="0 0 22 22" aria-hidden="true"><rect width="22" height="22" rx="4" fill="#2f9fdc"/><path d="M7 5c1 0 2 2 2 3s-1 1-1 2c1 2 2 3 4 4 1 0 1-1 2-1s3 1 3 2-1 2-2 2C10 17 5 12 5 7c0-1 1-2 2-2z" fill="#fff"/></svg>
        555-014-7730
      </li>
      <li>
        <svg viewBox="0 0 22 22" aria-hidden="true"><rect width="22" height="22" rx="4" fill="#2f9fdc"/><rect x="5" y="7" width="12" height="8" fill="none" stroke="#fff" stroke-width="1.5"/><path d="M5 7l6 5 6-5" fill="none" stroke="#fff" stroke-width="1.5"/></svg>
        youremail@mailbox.com
      </li>
      <li>
        <svg viewBox="0 0 22 22" aria-hidden="true"><rect width="22" height="22" rx="4" fill="#2f9fdc"/><circle cx="11" cy="11" r="6" fill="none" stroke="#fff" stroke-width="1.5"/><path d="M5 11h12M11 5c-3 3-3 9 0 12M11 5c3 3 3 9 0 12" fill="none" stroke="#fff" stroke-width="1.2"/></svg>
        www.yourwebsite.com
      </li>
    </ul>

    <div class="base-stripe"></div>
    <div class="corner-block"></div>
  </section>
</body>
</html>
```